Awesome photographers card for an awesome new business

Double sided business card Black background and silver logo in middle on one side. Details on otherside. please keep it simple

Photographer

Gavin Tolley
0482615073
GavinTolleyPhotography82@lumenpost.com
www.GavinTolleyPhotography.com.au
Instagram _Gavin_tolley

Requirements
Must have
• My logo in Silver
• please use instagram logo instead of "Instagram"

```html
<!DOCTYPE html>
<html lang="en">
<head>
<meta charset="utf-8">
<title>Gavin Tolley Photography – Business Card</title>
<link rel="stylesheet" href="https://fonts.googleapis.com/css2?family=Lato:wght@400;700&display=swap">
<style>
  :root {
    --backdrop: #1b1b1b;
    --card-dark: #121212;
    --card-light: #262626;
    --silver: #c9c9c9;
    --text: #f2f2f2;
  }
  html, body {
    margin: 0;
    width: 1200px;
    height: 897px;
    overflow: hidden;
    background: var(--backdrop);
    font-family: "Lato", sans-serif;
  }
  .canvas {
    position: relative;
    width: 1200px;
    height: 897px;
  }
  .card {
    position: absolute;
    background: radial-gradient(ellipse at 85% 55%, var(--card-light) 0%, var(--card-dark) 70%);
    box-shadow: 0 10px 24px rgba(0,0,0,0.6);
  }
  .card-front {
    left: 354px;
    top: 160px;
    width: 486px;
    height: 278px;
  }
  .card-back {
    left: 348px;
    top: 468px;
    width: 492px;
    height: 278px;
  }
  .brand-mark {
    position: absolute;
    left: 167px;
    top: 74px;
    width: 152px;
    height: 152px;
  }
  .brand-mark circle {
    fill: none;
    stroke: var(--silver);
    stroke-width: 3;
  }
  .brand-name {
    position: absolute;
    left: 167px;
    width: 152px;
    top: 143px;
    line-height: 14px;
    text-align: center;
    color: var(--silver);
    font-size: 12px;
    font-weight: 400;
    letter-spacing: 2px;
    text-transform: uppercase;
    white-space: nowrap;
  }
  .front-url {
    position: absolute;
    left: 0;
    right: 0;
    top: 247px;
    text-align: center;
    color: var(--text);
    font-size: 12px;
    letter-spacing: 1.2px;
  }
  .holder-name {
    position: absolute;
    right: 22px;
    top: 26px;
    color: var(--text);
    font-size: 13px;
    font-weight: 400;
    letter-spacing: 2.4px;
    text-transform: uppercase;
  }
  .contact-list {
    position: absolute;
    left: 24px;
    top: 193px;
    margin: 0;
    padding: 0;
    list-style: none;
  }
  .contact-item {
    display: flex;
    align-items: center;
    height: 15.6px;
    color: var(--text);
    font-size: 11.5px;
    letter-spacing: 0.3px;
  }
  .contact-icon {
    width: 9px;
    height: 9px;
    margin-right: 10px;
    flex: none;
  }
  .contact-icon * {
    fill: none;
    stroke: var(--text);
    stroke-width: 1.3;
  }
  .contact-icon .solid {
    fill: var(--text);
    stroke: none;
  }
</style>
</head>
<body>
<main class="canvas">
  <section class="card card-front" aria-label="Card front">
    <svg class="brand-mark" viewBox="0 0 152 152" aria-hidden="true">
      <circle cx="76" cy="76" r="72"/>
    </svg>
    <div class="brand-name">Gavin Tolley</div>
    <div class="front-url">GavinTolleyPhotography.com.au</div>
  </section>

  <section class="card card-back" aria-label="Card back">
    <div class="holder-name">Gavin Tolley</div>
    <ul class="contact-list">
      <li class="contact-item">
        <svg class="contact-icon" viewBox="0 0 10 10" aria-hidden="true">
          <path class="solid" d="M1 1.2 L3 0.6 L4.2 3 L3 4 Q4 6 6 7 L7 5.8 L9.4 7 L8.8 9 Q4.5 9 1 5.5 Q0.8 3 1 1.2Z"/>
        </svg>
        0482615073
      </li>
      <li class="contact-item">
        <svg class="contact-icon" viewBox="0 0 10 10" aria-hidden="true">
          <rect class="solid" x="0.5" y="2" width="9" height="6.5"/>
        </svg>
        GavinTolleyPhotography82@lumenpost.com
      </li>
      <li class="contact-item">
        <svg class="contact-icon" viewBox="0 0 10 10" aria-hidden="true">
          <circle cx="5" cy="5" r="4.2"/>
          <ellipse cx="5" cy="5" rx="1.8" ry="4.2"/>
          <line x1="0.8" y1="5" x2="9.2" y2="5"/>
        </svg>
        www.GavinTolleyPhotography.com.au
      </li>
      <li class="contact-item">
        <svg class="contact-icon" viewBox="0 0 10 10" aria-hidden="true">
          <rect x="1" y="1" width="8" height="8"/>
        </svg>
        _Gavin_tolley
      </li>
    </ul>
  </section>
</main>
</body>
</html>
```